Etiketten-Design für Produkte eines Familienbetriebs mit Imkerei und Hühnerhaltung
Zielgruppe
Wir sind ein Familienbetrieb mit Imkerei und Hühnerhaltung. Wir suchen für unsere Produkte ein modernes Corporate Design, mit zentralen, bei jedem Produkt vorkommenden Elementen, sowie Elementen, welche produktindividuell sind.
Wir leben in einem 150 jährigen Riegelhaus, welches in der Umgebung sehr bekannt ist. Es soll im Etiketten-Design zentral erscheinen.
Unsere Produkte sind: Honig, Pollen, Eier
Aufgabenstellung
1. Zentrale, auf allen Etiketten wiederkehrende Elemente:
- Unser Riegelhaus (stilisiert) (Bild beiliegend)
- Das Wort 'Birkeneck' (Anmerkung: ohne Anführungszeichen)
- die zentralen Elemente sollen die Produkte nicht überragen.
2. Dezente Adresse:
- Familie Dorbach, Birkeneck, CH-9573 Holtikon
3. Produkte:
a) Honig
Sorten: Waldhonig (dunkel), Blütenhonig (gelblich-goldig), Crèmehonig (gelblich-weisslich), Lavendelhonig (gelblich-goldig)
Die Honigsorten sollen farblich hervortreten.
Freifeld (zweizeilig): für die Lotnummer und die Haltbarkeitsangabe)
Gewicht: 250 g, 500 g
b) Pollen
Gewicht: 100 g
c) Eier
Verpackungseinheiten: 4er-, 6er-, 10er-Packung
Haltungsform: BIO-Haltung
das Wort 'frisch'
Farbe grün (=Bio) soll farblich hervortreten (ähnlich wie beim Honig)
Freifeld (zweizeilig: für das Eigewicht und die Haltbarkeitsangabe)
Bitte keine Stock-Bilder verwenden. Die Etiketten sollen schlicht, edel ,schörkellos und modern erscheinen.
Das Etikett soll Exklusivität und Qualität ausstrahlen. Etikettenhintergrund einfarbig.
Interessanterweise gibt es bei Weinen solche Etiketten. Ich habe einige rausgesucht und angehängt, um die Richtung vorzugeben. (Wein1-6)
Ich habe auch eine schlichte Honigetikette gefunden, die ins Schema passt. (Imker1)
Zusätzlich sind jetzt auch noch Farbbeispiele der Honigsorten zur besseren Abstimmung von Inhalt und Etikette beigelegt. Lavendelhonig ist dem Blütenhonig sehr ähnlich.
Etikettengrössen:
Honig/Pollen 250 g: 190 x 42 mm
Honig 500 g: 206 x 45 mm
Eier 4er: 60 x 60 mm
Eier 6er: 110 x 60 mm
Eier 10er: 170 x 60 cm

```html
<!DOCTYPE html>
<html lang="de">
<head>
<meta charset="utf-8">
<title>Etiketten Frisch Eier – Familie Dorbach</title>
<link href="https://fonts.googleapis.com/css2?family=Montserrat:ital,wght@0,400;0,500;0,600;1,400&display=swap" rel="stylesheet">
<style>
  :root {
    --page: #ffffff;
    --sage: #d3dfd8;
    --sage-ink: #2b2b2b;
    --bio-green: #64825c;
    --bio-ink: #ffffff;
    --field-light: #ffffff;
    --field-pale: #d3dcd5;
    --photo-top: #6f7771;
    --photo-bottom: #a9b1ab;
  }
  * { margin: 0; padding: 0; box-sizing: border-box; }
  html, body {
    width: 1200px; height: 2422px; overflow: hidden;
    background: var(--page);
    font-family: "Montserrat", sans-serif;
  }
  .label {
    position: absolute; left: 56px; width: 1083px; overflow: hidden;
  }
  .label--ten { top: 38px; height: 570px; background: var(--sage); color: var(--sage-ink); }
  .label--six { top: 631px; height: 588px; background: var(--bio-green); color: var(--bio-ink); }

  .label__husbandry { position: absolute; font-size: 21px; font-weight: 500; white-space: nowrap; }
  .label--ten .label__husbandry { left: 19px; top: 14px; }
  .label--six .label__husbandry { left: 32px; top: 18px; font-weight: 600; }

  .label__address { position: absolute; font-size: 22px; line-height: 26px; font-style: normal; white-space: nowrap; }
  .label--ten .label__address { left: 23px; top: 367px; }
  .label--six .label__address { left: 37px; top: 346px; font-weight: 500; }

  .label__field { position: absolute; }
  .label--ten .label__field { left: 23px; width: 180px; height: 39px; background: var(--field-light); }
  .label--ten .label__field--first { top: 459px; }
  .label--ten .label__field--second { top: 516px; }
  .label--six .label__field { left: 33px; width: 159px; height: 37px; background: var(--field-pale); }
  .label--six .label__field--first { top: 470px; }
  .label--six .label__field--second { top: 520px; }

  .label__count {
    position: absolute; text-align: right; font-size: 24px; padding-right: 14px;
  }
  .label--ten .label__count { left: 875px; top: 516px; width: 180px; height: 39px; line-height: 42px; background: var(--field-light); }
  .label--six .label__count { left: 887px; top: 520px; width: 159px; height: 37px; line-height: 38px; background: var(--field-pale); color: #3a3a3a; font-weight: 600; font-size: 22px; }

  .label__photo {
    position: absolute;
    background: linear-gradient(180deg, var(--photo-top) 0%, var(--photo-bottom) 100%);
  }
  .label--ten .label__photo { left: 365px; top: 172px; width: 353px; height: 226px; }
  .label--six .label__photo { left: 359px; top: 136px; width: 441px; height: 252px; }

  .label__rule { position: absolute; left: 366px; top: 393px; width: 390px; height: 3px; background: var(--bio-ink); }

  .label__farm { position: absolute; text-align: center; white-space: nowrap; }
  .label--ten .label__farm { left: 313px; width: 400px; top: 421px; font-size: 26px; font-style: italic; }
  .label--six .label__farm { left: 343px; width: 400px; top: 414px; font-size: 22px; font-weight: 500; }

  .label__arcs { position: absolute; left: 0; top: 0; width: 1083px; height: 588px; }
  .arc-text { font-family: "Montserrat", sans-serif; font-weight: 600; }
  .label--ten .arc-text { fill: var(--sage-ink); }
  .label--six .arc-text { fill: var(--bio-ink); }
</style>
</head>
<body>

<section class="label label--ten">
  <p class="label__husbandry">Haltungsform: BIO-Haltung</p>
  <div class="label__photo" role="img" aria-label="Foto des Riegelhauses Birkeneck"></div>
  <svg class="label__arcs" viewBox="0 0 1083 588">
    <defs>
      <path id="ten-family-arc" d="M 330,185 Q 515,40 700,185"/>
      <path id="ten-product-arc" d="M 370,500 Q 513,532 660,500"/>
    </defs>
    <text class="arc-text" font-size="45"><textPath href="#ten-family-arc" startOffset="50%" text-anchor="middle">Familie Dorbach</textPath></text>
    <text class="arc-text" font-size="45"><textPath href="#ten-product-arc" startOffset="50%" text-anchor="middle">Frisch Eier</textPath></text>
  </svg>
  <p class="label__farm">Birkeneck 1870</p>
  <address class="label__address">Familie Dorbach<br>Birkeneck,<br>CH-9573 Holtikon</address>
  <div class="label__field label__field--first"></div>
  <div class="label__field label__field--second"></div>
  <p class="label__count">10 er</p>
</section>

<section class="label label--six">
  <p class="label__husbandry">Haltungsform: BIO-Haltung</p>
  <div class="label__photo" role="img" aria-label="Foto des Riegelhauses Birkeneck"></div>
  <div class="label__rule"></div>
  <svg class="label__arcs" viewBox="0 0 1083 588">
    <defs>
      <path id="six-family-arc" d="M 350,152 Q 545,14 745,152"/>
      <path id="six-product-arc" d="M 390,505 Q 540,552 690,505"/>
    </defs>
    <text class="arc-text" font-size="48"><textPath href="#six-family-arc" startOffset="50%" text-anchor="middle">Familie Dorbach</textPath></text>
    <text class="arc-text" font-size="46"><textPath href="#six-product-arc" startOffset="50%" text-anchor="middle">Frisch Eier</textPath></text>
  </svg>
  <p class="label__farm">Birkeneck 1870</p>
  <address class="label__address">Familie Dorbach<br>Birkeneck,<br>CH-9573 Holtikon</address>
  <div class="label__field label__field--first"></div>
  <div class="label__field label__field--second"></div>
  <p class="label__count">6 er</p>
</section>

</body>
</html>
```